Hong Kong residential leasing and sales company needs a website design

Hong Kong has many competitive real estate agents. The majority of us have the same listings so, besides the team and experience, a website is what makes us stand out. A first impression. We need our website to be user friendly, informative and to have a wow factor. Most sites are generic so whilst we are close to accepting that maybe that's the only formula which works....we would like to see if we're missing something! Our clients are a mix of International users of all ages but probably ultimately 35+.. We have a logo (attached) which we would like to keep - designed by artmarketly. Flexible with colours except red.
examples of our competitors are:
http://www.brindlewoodestates.example
http://www.nuvo.example/home
http://www.premierdwellingsvx.example
http://www.orchid-lettings.example
http://www.tidemark-harrowgates.example
We were thinking of having the following in a menu bar with drop downs for most...some more than others. Home / For Sale / For Rent / Property 101 / About us / Contact Us ..
Look forward to seeing your ideas. Thanks in advance.

```html
<!DOCTYPE html>
<html lang="en">
<head>
<meta charset="utf-8">
<title>Harbourline Homes – Hong Kong Property</title>
<link href="https://fonts.googleapis.com/css2?family=Open+Sans:wght@400;600;700&display=swap" rel="stylesheet">
<style>
:root{
  --purple:#8a3bb8;
  --purple-dark:#6f2b98;
  --ink:#3d3d3d;
  --muted:#7a7a7a;
  --line:#d9d9d9;
  --grey-band:#f3f3f3;
  --bubble:#8c8c8c;
  --dark:#2a2a2a;
  --page:#ffffff;
  --outside:#f5f5f5;
}
*{box-sizing:border-box;margin:0;padding:0}
html,body{width:720px;height:1200px;overflow:hidden}
body{background:var(--outside);font-family:'Open Sans',Arial,sans-serif;color:var(--ink);position:relative}
.page{position:absolute;left:60px;top:0;width:600px;height:1030px;background:var(--page)}
.abs{position:absolute}

/* header */
.brand{left:76px;top:14px;display:flex;align-items:center;gap:6px}
.brand-mark{width:14px;height:14px;background:var(--purple)}
.brand-name{font-size:14px;font-weight:700;color:var(--purple);letter-spacing:1px;line-height:1.1;width:80px}
.phone{left:422px;top:22px;display:flex;align-items:center;gap:8px;font-size:10px;color:var(--muted)}
.search-box{left:530px;top:23px;width:116px;height:16px;border:1px solid var(--line);background:#fff}
.search-btn{left:627px;top:23px;width:19px;height:16px;background:var(--purple)}
.nav{left:267px;top:48px;display:flex;align-items:center;font-size:9px;color:var(--ink)}
.nav a{color:inherit;text-decoration:none;margin-right:26px}
.nav .active{border:1px solid var(--purple);border-radius:10px;padding:3px 10px;color:var(--purple);font-weight:600;margin-right:16px}

/* hero */
.hero{left:76px;top:81px;width:570px;height:266px;border:1px solid var(--line);background:linear-gradient(90deg,#b8d99a 0%,#eef4e4 40%,#f4f4ef 70%,#dfe9d0 100%)}
.hero-arrow{top:206px;width:15px;height:15px;border-radius:50%;background:rgba(0,0,0,.12)}
.finder{left:408px;top:154px;width:148px;height:143px;background:rgba(220,220,220,.85)}
.finder-tabs{display:flex;font-size:9px;color:#fff;font-weight:600}
.finder-tabs span{flex:1;height:25px;line-height:25px;text-align:center}
.tab-sale{background:#3b3b3b}.tab-rent{background:#8a8a8a}
.finder-input{position:absolute;left:10px;top:50px;width:127px;height:23px;background:#fff;font-size:7.5px;color:#999;line-height:23px;padding-left:7px}
.finder-btn{position:absolute;left:10px;top:86px;width:127px;height:22px;background:var(--purple);color:#fff;font-size:9px;font-weight:600;text-align:center;line-height:22px}
.finder-count{position:absolute;left:0;top:116px;width:100%;text-align:center;font-size:7.5px;color:var(--ink)}
.dots{left:339px;top:354px;display:flex;gap:6px}
.dots i{width:6px;height:6px;border-radius:50%;background:#ccc}
.dots i:first-child{background:var(--purple)}

/* tabs */
.listing-tabs{left:76px;top:379px;display:flex;align-items:center;font-size:9.5px;color:var(--muted)}
.listing-tabs .current{background:var(--purple);color:#fff;padding:3px 11px;position:relative;margin-right:36px}
.listing-tabs .current:after{content:"";position:absolute;left:50%;bottom:-5px;margin-left:-5px;border:5px solid transparent;border-bottom:0;border-top-color:var(--purple)}
.listing-tabs .sep{margin:0 18px}

/* cards */
.card{width:127px;height:157px;border:1px solid var(--line);background:#fff;text-align:center}
.card.raised{box-shadow:0 2px 8px rgba(0,0,0,.18);border-color:#eee}
.card-photo{margin:5px auto 0;width:116px;height:84px}
.card-title{font-size:8px;font-weight:700;margin-top:5px;color:var(--ink)}
.card-meta{font-size:7px;color:var(--muted);line-height:10px;margin-top:2px}
.card-foot{position:absolute;left:0;bottom:0;width:100%;height:18px;border-top:1px solid var(--line);display:flex;font-size:7.5px;line-height:17px}
.card-foot span{flex:1}
.card-foot span+span{border-left:1px solid var(--line)}
.raised .price{background:#9a9a9a;color:#fff}

/* week + reviews */
.section-title{font-size:11px;font-weight:600;color:#555}
.week-photo{left:73px;top:815px;width:220px;height:168px;background:linear-gradient(180deg,#eeeae4 0%,#ddd6cc 55%,#a33040 75%,#d8d8d8 100%)}
.week-info{left:308px;top:813px;width:139px}
.week-info h3{font-size:9.5px;font-weight:400;color:var(--ink)}
.week-info .ref{font-size:7px;margin-top:3px}
.week-info p{font-size:7px;color:var(--muted);line-height:10px;margin-top:14px;text-align:justify}
.week-info .meta{margin-top:4px;text-align:left}
.week-info .price{color:var(--purple);font-size:9px;margin-top:8px}
.week-btn{display:inline-block;margin-top:11px;background:var(--purple);color:#fff;font-size:8.5px;padding:3px 10px}
.review{left:468px;width:178px;height:48px}
.avatar{position:absolute;left:0;top:0;width:33px;height:33px;border-radius:50%;border:2px solid #ddd;background:#c8c0b8}
.review-name{position:absolute;left:0;top:35px;font-size:5px;font-weight:700;line-height:6px;color:#333}
.bubble{position:absolute;left:53px;top:2px;width:125px;height:46px;background:var(--bubble);color:#eee;font-size:5.5px;line-height:9.5px;padding:5px 6px;box-shadow:0 2px 0 #ccc}
.bubble:before{content:"";position:absolute;left:-7px;top:8px;border:5px solid transparent;border-right:7px solid var(--bubble);border-left:0}

/* footer */
.footer{left:0;top:1030px;width:720px;height:135px;background:var(--grey-band)}
.foot-col{top:1055px;font-size:7px;color:#555;line-height:15px}
.foot-col h4{font-size:8.5px;color:var(--purple);font-weight:600;margin-bottom:5px}
.news{display:flex;gap:8px;margin-bottom:10px;line-height:9px}
.news-thumb{width:25px;height:25px;background:linear-gradient(135deg,#2d3f7a,#7e8fbf)}
.news b{font-size:7.5px;color:#333}
.news small{font-size:5.5px;display:block}
.social{display:flex;align-items:center;gap:8px;font-size:8.5px;margin-bottom:10px}
.social i{width:14px;height:14px;background:#bbb;display:block}
.bottom-bar{left:0;top:1165px;width:720px;height:35px;background:var(--dark);color:#eee;font-size:7px;text-align:center;line-height:35px}
</style>
</head>
<body>
<div class="page"></div>

<header>
  <div class="abs brand"><span class="brand-mark"></span><span class="brand-name">Harbourline Homes</span></div>
  <div class="abs phone">
    <svg width="14" height="14" viewBox="0 0 14 14"><circle cx="7" cy="7" r="6.3" fill="none" stroke="#aaa"/><path d="M5 4c-1 1 0 4 2 5s2 1 3 0l-1-1-1 .5c-1-.5-1.5-1-2-2l.5-1z" fill="#aaa"/></svg>
    0141 555 0192</div>
  <div class="abs search-box"></div>
  <div class="abs search-btn"><svg width="19" height="16" viewBox="0 0 19 16"><circle cx="9" cy="7" r="3.2" fill="none" stroke="#fff" stroke-width="1.4"/><path d="M11.3 9.3l2.5 2.5" stroke="#fff" stroke-width="1.6"/></svg></div>
  <nav class="abs nav">
    <a class="active" href="#">&#8962; Home</a><a href="#">For Sale</a><a href="#">For Rent</a><a href="#">Property 101</a><a href="#">About us</a><a href="#" style="margin-right:0">Contact Us</a>
  </nav>
</header>

<section>
  <div class="abs hero" role="img" aria-label="Smiling woman in a green cardigan relaxing on a sofa in a bright living room"></div>
  <span class="abs hero-arrow" style="left:100px"></span>
  <span class="abs hero-arrow" style="left:611px"></span>
  <div class="abs finder">
    <div class="finder-tabs"><span class="tab-sale">FOR SALE</span><span class="tab-rent">FOR RENT</span></div>
    <div class="finder-input">Type Building or street Name &#9662;</div>
    <div class="finder-btn">SEARCH</div>
    <div class="finder-count">3,029 properties in HONG KONG</div>
  </div>
  <div class="abs dots"><i></i><i></i><i></i></div>
</section>

<section>
  <div class="abs listing-tabs">
    <span class="current">Featured Properties</span>New Additions<span class="sep">|</span>For Rent<span class="sep">|</span>For Sale<span class="sep">|</span>Serviced Apartments
  </div>

  <div class="abs card raised" style="left:76px;top:425px"><div class="card-photo" role="img" aria-label="Apartment balcony with city view" style="background:linear-gradient(180deg,#cfd6da,#8a8f8c 60%,#a8523e)"></div><div class="card-title">Morning Light Apartments</div><div class="card-meta">SA1,400 sq ft / GA1,800 sq ft<br>3 bedrooms, 2 bathrooms</div><div class="card-foot"><span class="price">HK$55,000</span><span>Ref. #: 6731</span></div></div>
  <div class="abs card" style="left:223px;top:425px"><div class="card-photo" role="img" aria-label="Modern living room interior" style="background:linear-gradient(90deg,#e8e4dc,#d8cdbd 60%,#3a3430)"></div><div class="card-title">Lorem ipsum dolor</div><div class="card-meta">SA1,400 sq ft / GA1,800 sq ft<br>3 bedrooms, 2 bathrooms</div><div class="card-foot"><span>HK$55,000</span><span>Ref. #: 6731</span></div></div>
  <div class="abs card" style="left:371px;top:425px"><div class="card-photo" role="img" aria-label="Lounge with curved orange sofa" style="background:linear-gradient(180deg,#c98a3c,#e6c48a 50%,#d8a020)"></div><div class="card-title">Dolor sit amit contantry</div><div class="card-meta">SA1,400 sq ft / GA1,800 sq ft<br>3 bedrooms, 2 bathrooms</div><div class="card-foot"><span>HK$55,000</span><span>Ref. #: 6731</span></div></div>
  <div class="abs card" style="left:518px;top:425px"><div class="card-photo" role="img" aria-label="White living room with sofas" style="background:linear-gradient(180deg,#d8d8d8,#f2f2f2 60%,#555)"></div><div class="card-title">Contantry popilar</div><div class="card-meta">SA1,400 sq ft / GA1,800 sq ft<br>3 bedrooms, 2 bathrooms</div><div class="card-foot"><span>HK$55,000</span><span>Ref. #: 6731</span></div></div>

  <div class="abs card" style="left:76px;top:601px"><div class="card-photo" role="img" aria-label="Living room with framed pictures" style="background:linear-gradient(90deg,#3a3a3a,#e8e4dc 40%,#b59070)"></div><div class="card-title">Lorem ipsum dolor</div><div class="card-meta">SA1,400 sq ft / GA1,800 sq ft<br>3 bedrooms, 2 bathrooms</div><div class="card-foot"><span>HK$55,000</span><span>Ref. #: 6731</span></div></div>
  <div class="abs card" style="left:223px;top:601px"><div class="card-photo" role="img" aria-label="Modern kitchen with breakfast bar" style="background:linear-gradient(180deg,#2a2a2a,#f0f0f0 55%,#3a2a22)"></div><div class="card-title">Lorem ipsum dolor</div><div class="card-meta">SA1,400 sq ft / GA1,800 sq ft<br>3 bedrooms, 2 bathrooms</div><div class="card-foot"><span>HK$55,000</span><span>Ref. #: 6731</span></div></div>
  <div class="abs card" style="left:371px;top:601px"><div class="card-photo" role="img" aria-label="Purple bedroom" style="background:linear-gradient(180deg,#7a4a7a,#b08ab0 50%,#6a4a6a)"></div><div class="card-title">Dolor sit amit contantry</div><div class="card-meta">SA1,400 sq ft / GA1,800 sq ft<br>3 bedrooms, 2 bathrooms</div><div class="card-foot"><span>HK$55,000</span><span>Ref. #: 6731</span></div></div>
  <div class="abs card" style="left:518px;top:601px"><div class="card-photo" role="img" aria-label="Bedroom with teal curtains" style="background:linear-gradient(90deg,#e6e0d6,#f2eee8 50%,#4fb0a8)"></div><div class="card-title">Contantry popilar</div><div class="card-meta">SA1,400 sq ft / GA1,800 sq ft<br>3 bedrooms, 2 bathrooms</div><div class="card-foot"><span>HK$55,000</span><span>Ref. #: 6731</span></div></div>
</section>

<section>
  <h2 class="abs section-title" style="left:75px;top:790px">Property Of The Week</h2>
  <div class="abs week-photo" role="img" aria-label="Living room with red sofas and chandelier"></div>
  <div class="abs week-info">
    <h3>Lorem ipsum dolorsit amit</h3>
    <div class="ref">Ref. #: 6731</div>
    <p>reader will be distracted by the readable content of a page when looking at its layout. The point of using Lorem Ipsum is that it has a</p>
    <p class="meta">SA1,400 sq ft / GA1,800 sq ft<br>3 bedrooms, 2 bathrooms</p>
    <div class="price">HK$55,000</div>
    <span class="week-btn">House For Sale</span>
  </div>

  <h2 class="abs section-title" style="left:468px;top:788px">What people say</h2>
  <div class="abs review" style="top:812px"><span class="avatar" role="img" aria-label="Client portrait"></span><span class="review-name">SARAH DOE<br>CEO, COMPANY.COM</span><div class="bubble">Because we know you don't want to be limited on a portrait or scape format we made Showcase.</div></div>
  <div class="abs review" style="top:880px"><span class="avatar" role="img" aria-label="Client portrait"></span><span class="review-name">SARAH DOE<br>CEO, COMPANY.COM</span><div class="bubble">Because we know you don't want to be limited on a portrait or scape format we made Showcase.</div></div>
  <div class="abs review" style="top:950px"><span class="avatar" role="img" aria-label="Client portrait"></span><span class="review-name">SARAH DOE<br>CEO, COMPANY.COM</span><div class="bubble">Because we know you don't want to be limited on a portrait or scape format we made Showcase.</div></div>
</section>

<footer>
  <div class="abs footer"></div>
  <div class="abs foot-col" style="left:75px"><h4>Need help?</h4>Our Services<br>Timesheets<br>FAQ<br>Terms and Conditions</div>
  <div class="abs foot-col" style="left:206px"><h4>User area</h4>Our Services<br>FAQ<br>Terms and Conditions</div>
  <div class="abs foot-col" style="left:344px;width:200px">
    <h4>Latest News</h4>
    <div class="news"><span class="news-thumb" role="img" aria-label="News thumbnail"></span><div><b>Lorem ipsum</b><small>simply dummy text of the printing and typesetting</small><small><b style="font-size:5.5px">Feb - 14 - 2014</b></small></div></div>
    <div class="news"><span class="news-thumb" role="img" aria-label="News thumbnail" style="background:linear-gradient(135deg,#e8e0d8,#a04040)"></span><div><b>Lorem ipsum</b><small>simply dummy text of the printing and typesetting</small><small><b style="font-size:5.5px">Feb - 14 - 2014</b></small></div></div>
  </div>
  <div class="abs foot-col" style="left:579px"><h4>Get In Touch</h4>
    <div class="social"><i></i>Linkup</div>
    <div class="social"><i></i>Chirper</div>
  </div>
  <div class="abs bottom-bar">Copyright yoursite.com | Site Map | Contact Details | Privacy Policy</div>
</footer>
</body>
</html>
```